依頼詳細
サイズ:縦1400px(テンプレートをご参照ください)
解像度:150dpi以上
記載項目
【1】
ロゴ:勤め人の座右本
ショルダー:できる新入社員になる
タイトル:社会人の言葉えらび帳
著者:仕事人倶楽部ミルテ
コピー:「不躾なお願いで恐縮ですが」は上司に使っちゃいけません!

【2】
ロゴ:勤め人の座右本
ショルダー:できる社会人はココが違う!
タイトル:手ごわい先輩と上手に付き合う方法
著者:仕事人倶楽部ミルテ
コピー:新入社員必見!イヤな上司、困った上司、残念な上司・・・どんな上司も味方に変える「上司の取扱説明書」

【3】
ロゴ:勤め人の座右本
ショルダー:ビジネスマンだからできる!
タイトル:検定突破法
著者:仕事人倶楽部ミルテ
コピー:働きながらでも、時間がなくても無理なく続けるコツを集約!

※コピーの改行位置はデザインによりお任せします。
※コピーは帯ふうにしていただいてもかまいません。
希望イメージ
シンプル 複雑
単色 カラフル
暗い 明るい
日常 高級
遊び心 厳粛
未来的 伝統的
女性的 男性的
希望する色
特になし
納品ファイル
• 高解像度JPG (.jpg)
• イラストレーター形式 (.ai)
補足説明
フレームデザインのファイルをアップしました
フレームデザインのファイルをアップしました
● ご提案くださったみなさまへ
はじめてソメリカを利用させていただきました。
想像以上に多くのご提案をいただき、
その量と質にとても驚いています。

どのご提案も本当に素晴らしかったのですが、今回は下記の理由で、
taviさまのご提案を採用させていただくことになりました。
一つしか選定できなくて申し訳ありません。
時間をかけてご提案いただき、どうもありがとうございました。

弊社はこれからも、多くの電子書籍を制作していく予定です。
(現在も、あと4点の表紙を募集しています)
今回残念ながら、採用させていただくことができなかった方も、
また、別件でご提案いただけますと嬉しいです。
何卒よろしくお願いいたします。

● 選定の理由
・タイトルが読みやすいこと
・フォントが凝っていて紙の実用書ふうであるころ
・色合いがさわやかで新入社員向けの雰囲気が出ていること
■ 選んだ理由

・タイトルが読みやすいこと
・フォントが凝っていて紙の実用書ふうであるころ

■ 提案者全員のお礼・コメント

※「依頼詳細」に全文追記させていただきました。

はじめてソメリカを利用させていただきました。
想像以上に多くのご提案をいただき、
その量と質にとても驚いています。

どのご提案も本当に素晴らしかったのですが、今回は上記の理由で、
一つしか選定できなくて申し訳ありません。

```html
<!DOCTYPE html>
<html lang="ja">
<head>
<meta charset="utf-8">
<title>社会人の言葉えらび帳</title>
<link rel="stylesheet" href="https://fonts.googleapis.com/css2?family=M+PLUS+1p:wght@500;700;800;900&display=swap">
<style>
  :root {
    --paper: #ffffff;
    --ink: #1d1d1d;
    --navy: #1c3f6e;
    --accent: #1d8fd2;
    --band: #a5d7f1;
    --badge: #cfe9f8;
  }
  html, body {
    margin: 0;
    padding: 0;
    overflow: hidden;
    background: var(--paper);
  }
  .cover {
    position: relative;
    width: 837px;
    height: 1200px;
    background: var(--paper);
    overflow: hidden;
    font-family: "M PLUS 1p", sans-serif;
    color: var(--ink);
  }
  .series-mark {
    position: absolute;
    left: 48px;
    top: 18px;
    width: 150px;
    height: 150px;
    border-radius: 50%;
    background: var(--badge);
    display: flex;
    align-items: center;
    justify-content: center;
    text-align: center;
    font-weight: 800;
    font-size: 30px;
    line-height: 1.15;
    color: var(--navy);
  }
  .publisher {
    position: absolute;
    right: 22px;
    top: 0;
    width: 86px;
    height: 98px;
    background: var(--navy);
    color: var(--paper);
    font-weight: 700;
    font-size: 19px;
    line-height: 1.2;
    display: flex;
    align-items: center;
    justify-content: center;
    text-align: center;
  }
  .shoulder {
    position: absolute;
    left: 222px;
    top: 52px;
    font-weight: 800;
    color: var(--navy);
    line-height: 1.1;
  }
  .shoulder .lead { display: block; font-size: 38px; padding-left: 44px; }
  .shoulder .main { display: block; font-size: 42px; }
  .author {
    position: absolute;
    left: 700px;
    top: 140px;
    writing-mode: vertical-rl;
    font-weight: 700;
    font-size: 31px;
    letter-spacing: 0.04em;
    color: var(--ink);
  }
  .title {
    position: absolute;
    left: 62px;
    top: 190px;
    margin: 0;
    width: 630px;
    font-weight: 900;
    line-height: 1;
  }
  .title-line {
    display: block;
    font-size: 148px;
    height: 170px;
    letter-spacing: -0.02em;
  }
  .title-line.accent { color: var(--accent); padding-left: 20px; }
  .rule {
    position: absolute;
    left: 66px;
    width: 620px;
    border-top: 6px dotted var(--ink);
  }
  .copy-band {
    position: absolute;
    left: 0;
    top: 732px;
    width: 837px;
    height: 468px;
    background: var(--band);
  }
  .copy-box {
    position: absolute;
    left: 70px;
    top: 790px;
    width: 697px;
    height: 320px;
    background: var(--paper);
    border-radius: 14px;
    text-align: center;
    box-sizing: border-box;
    padding-top: 28px;
  }
  .copy-lead {
    font-weight: 800;
    font-size: 40px;
    color: var(--ink);
    margin: 0 0 10px;
  }
  .copy-main {
    font-weight: 900;
    font-size: 96px;
    line-height: 1.1;
    color: var(--accent);
    margin: 0;
    letter-spacing: -0.02em;
  }
</style>
</head>
<body>
<div class="cover">
  <div class="series-mark">勤め人の<br>座右本</div>
  <div class="publisher">葉舟<br>ブックス</div>
  <div class="shoulder">
    <span class="lead">できる</span>
    <span class="main">新入社員になる</span>
  </div>
  <div class="author">仕事人倶楽部ミルテ</div>

  <h1 class="title">
    <span class="title-line">社会人の</span>
    <span class="title-line">言葉</span>
    <span class="title-line accent">えらび帳</span>
  </h1>
  <div class="rule" style="top:345px"></div>
  <div class="rule" style="top:515px"></div>
  <div class="rule" style="top:690px"></div>

  <div class="copy-band"></div>
  <div class="copy-box">
    <p class="copy-lead">「不躾なお願いで恐縮ですが」は</p>
    <p class="copy-main">上司に使っちゃ<br>いけません!</p>
  </div>
</div>
</body>
</html>
```